Graphic to show easy steps to find financial clarity

Howdy-I need a graphic that describe my Coin Harbor Method.The attached is a concept, but please use your own creativity to show how you would display this:- There are 5 steps the process (and then we repeat/recalculate)- And three bullets that drive home the results of the processI've also attached my logo. Please use the colors in my logo and maybe add a soft green as needed.The reader should be able to briefly scan this document and understand that this is an easy/simple process that tells them how to manage their cash.Thanks!-Ned

Target Market(s)

wealthy women, whether single or married

Requirements
Must have
• Please use the colors in my logo and a soft green if needed
Should not have
• This should be a very easy to read graphic that communicates how simple/easy this is to do.

```html
<!DOCTYPE html>
<html lang="en">
<head>
<meta charset="utf-8">
<title>Coin Harbor Method</title>
<link href="https://fonts.googleapis.com/css2?family=Bebas+Neue&family=Source+Sans+3:ital,wght@0,300;1,300&display=swap" rel="stylesheet">
<style>
  :root {
    --navy: #123a7c;
    --navy-band: #0f3470;
    --ink-soft: #555a63;
    --circle: #ffffff;
    --ring: #e4e6ea;
    --page: #ffffff;
  }
  * { margin: 0; padding: 0; box-sizing: border-box; }
  html, body { width: 1200px; height: 845px; overflow: hidden; background: var(--page); }
  .canvas { position: relative; width: 1200px; height: 845px; font-family: "Source Sans 3", sans-serif; }

  .brand { position: absolute; left: 450px; top: 186px; display: flex; align-items: center; gap: 10px; }
  .brand-square { width: 22px; height: 22px; background: var(--navy); }
  .brand-name { font-family: "Source Sans 3", sans-serif; font-weight: 300; font-size: 21px; color: var(--navy); letter-spacing: 0.5px; }

  .title { position: absolute; left: 0; width: 1142px; top: 250px; text-align: center; font-weight: 300; font-size: 40px; color: var(--navy); letter-spacing: 0.5px; }

  .track { position: absolute; left: 280px; top: 372px; width: 590px; height: 36px; background: var(--navy-band); }

  .repeat-arc { position: absolute; left: 852px; top: 326px; }

  .step { position: absolute; top: 348px; width: 92px; height: 92px; margin-left: -46px; border-radius: 50%; background: var(--circle); box-shadow: 0 6px 14px rgba(0,0,0,0.18); display: flex; align-items: center; justify-content: center; font-family: "Bebas Neue", sans-serif; font-size: 33px; color: var(--navy); letter-spacing: 0.5px; padding-top: 3px; }

  .step-label { position: absolute; top: 452px; width: 140px; margin-left: -70px; text-align: center; font-style: italic; font-weight: 300; font-size: 17px; line-height: 22px; color: var(--ink-soft); }

  .results { position: absolute; left: 324px; top: 553px; list-style: none; }
  .results li { position: relative; padding-left: 26px; font-style: italic; font-weight: 300; font-size: 17.5px; color: var(--ink-soft); height: 24px; line-height: 24px; }
  .results li + li { margin-top: 27px; }
  .results li::before { content: ""; position: absolute; left: 0; top: 7px; width: 11px; height: 11px; border-radius: 50%; background: var(--navy); box-shadow: 1px 2px 3px rgba(0,0,0,0.2); }
</style>
</head>
<body>
<div class="canvas">
  <div class="brand">
    <span class="brand-square"></span>
    <span class="brand-name">RIDGEWAY WEALTH MANAGEMENT, LLC</span>
  </div>

  <h1 class="title">COIN HARBOR METHOD</h1>

  <div class="track"></div>

  <svg class="repeat-arc" width="136" height="136" viewBox="0 0 136 136" aria-hidden="true">
    <path d="M 48 14 A 58 58 0 1 0 118 40" fill="none" stroke="var(--ring)" stroke-width="5"/>
    <path d="M 40 11 L 54 8 L 49 20 Z" fill="var(--ring)"/>
  </svg>

  <div class="step" style="left:234px">STEP 1</div>
  <div class="step" style="left:372px">STEP 2</div>
  <div class="step" style="left:509px">STEP 3</div>
  <div class="step" style="left:645px">STEP 4</div>
  <div class="step" style="left:782px">STEP 5</div>
  <div class="step" style="left:918px">REPEAT</div>

  <p class="step-label" style="left:234px">Know your annual spending</p>
  <p class="step-label" style="left:372px">Project special expenses</p>
  <p class="step-label" style="left:509px; width:100px; margin-left:-50px">Add up your 5-year cash needs</p>
  <p class="step-label" style="left:652px">Set them aside in savings</p>
  <p class="step-label" style="left:783px; top:457px">Invest the rest</p>
  <p class="step-label" style="left:929px; top:457px; width:170px; margin-left:-85px">Recalculate monthly</p>

  <ul class="results">
    <li>Know your lifestyle will be unaffected by the markets for at least 5 years.</li>
    <li>Spend intentionally and with joy</li>
    <li>Create a solid base for lifetime cash flow projections</li>
  </ul>
</div>
</body>
</html>
```